Harvest Gathering event flyer

I would like a church event flyer designed. The event is called "HARVEST GATHERING 2018". I am looking for a professional, yet catchy design that uses our brand colors and logo creatively while communicating key information of the event effectively.

1. The logo is attached in two color formats. The designer has the choice to use them as he/she want.

2. The location of the event is: Lindqvist Community Center, 482 Tamsworth Street, Portland, ME 04102
3. Time and date of event. The designer can organize and format the date and time as he/she pleases.
December 28th, 29th @ 7:00PM
December 30th @ 10:00AM
4. The topic of the event is "Tongues of fire". The designer is free to use this phrase as he/she pleases to create a good composition.
5. Speaker: Prophet Marcus Obuya
6. Contact information: contact@cedarbrookfellowship.org - Telephone number: 207 555 0148

7. I would also like the following three words on the flyer. These words describe the focus of the event: FIRE, REVIVAL, PROPHETIC

```html
<!DOCTYPE html>
<html lang="en">
<head>
<meta charset="utf-8">
<title>Harvest Gathering 2018 – Flyer</title>
<link href="https://fonts.googleapis.com/css2?family=Lato:wght@400;700;900&family=Great+Vibes&family=Libre+Baskerville&display=swap" rel="stylesheet">
<style>
  :root{
    --navy:#12345c;
    --orange:#f08c1a;
    --paper:#ffffff;
    --backdrop:#e6e6e6;
    --ghost:#ececec;
    --ink:#1d2f4a;
  }
  *{box-sizing:border-box;margin:0;padding:0}
  html,body{width:1200px;height:847px;overflow:hidden;background:var(--backdrop)}
  .flyer{position:absolute;left:290px;top:23px;width:620px;height:800px;background:var(--paper);overflow:hidden;font-family:"Lato",sans-serif;box-shadow:0 2px 8px rgba(0,0,0,.08)}
  .frame{position:absolute;left:22px;top:30px;right:22px;bottom:22px;border:2px solid var(--navy)}
  .brand{position:absolute;left:228px;top:16px;width:170px;height:170px;background:var(--navy);display:flex;align-items:center;justify-content:center;gap:10px}
  .brand-mark{width:14px;height:14px;background:var(--orange)}
  .brand-name{color:#fff;font-weight:700;font-size:28px;letter-spacing:1px}
  .title{position:absolute;top:206px;left:0;right:0;text-align:center;color:var(--orange);font-weight:900;font-size:40px;letter-spacing:.5px}
  .theme{position:absolute;top:258px;left:0;right:0;text-align:center;color:var(--navy);font-size:30px}
  .ghost-words{position:absolute;left:48px;top:336px;font-family:"Libre Baskerville",serif;font-size:38px;line-height:40px;color:var(--ghost);text-transform:uppercase}
  .speaker-label{position:absolute;left:246px;top:312px;font-size:15px;color:var(--ink);text-decoration:underline;letter-spacing:1px}
  .speaker-name{position:absolute;left:200px;top:330px;font-family:"Great Vibes",cursive;font-size:34px;color:#222;white-space:nowrap}
  .band-rule{position:absolute;left:22px;right:0;top:452px;height:2px;background:var(--navy)}
  .band{position:absolute;left:22px;right:0;top:462px;height:170px;background:var(--navy);padding:16px 0 0 46px;color:#fff}
  .band-rule.bottom{top:642px}
  .date{font-weight:700;font-size:22px;line-height:30px;white-space:nowrap}
  .date sup{font-size:12px;line-height:0}
  .time{font-size:16px;display:inline-flex;align-items:center;gap:4px;margin-left:6px;vertical-align:middle}
  .divider{width:300px;height:2px;background:var(--orange);margin:4px 0 6px}
  .venue{display:flex;gap:12px;color:var(--orange);font-weight:700;font-size:17px;line-height:21px;margin-top:8px}
  .contact{position:absolute;left:58px;top:666px;list-style:none;color:var(--ink);font-size:17px;line-height:32px}
  .contact li{display:flex;align-items:center;gap:12px}
  .speaker-photo{position:absolute;left:420px;top:400px;width:180px;height:378px;background:linear-gradient(180deg,#4a4a4a 0%,#2a2a2e 45%,#151518 100%);border-radius:90px 90px 0 0}
</style>
</head>
<body>
<article class="flyer">
  <div class="frame"></div>

  <div class="brand">
    <span class="brand-mark"></span>
    <span class="brand-name">CORVANE</span>
  </div>

  <h1 class="title">HARVEST GATHERING 2018</h1>
  <p class="theme">“ Tongues of Fire ”</p>

  <div class="ghost-words">Fire<br>Revival<br>Prophetic</div>

  <p class="speaker-label">Speaker:</p>
  <p class="speaker-name">Prophet Marcus Obuya</p>

  <div class="band-rule"></div>
  <section class="band">
    <p class="date">December 28<sup>th</sup>, 29<sup>th</sup><span class="time"><svg width="14" height="14" viewBox="0 0 14 14"><circle cx="7" cy="7" r="6" fill="none" stroke="#f08c1a" stroke-width="1.5"/><path d="M7 3.5V7l2 1.5" fill="none" stroke="#f08c1a" stroke-width="1.5"/></svg>7:00PM</span></p>
    <div class="divider"></div>
    <p class="date">December 30<sup>th</sup><span class="time"><svg width="14" height="14" viewBox="0 0 14 14"><circle cx="7" cy="7" r="6" fill="none" stroke="#fff" stroke-width="1.5"/><path d="M7 3.5V7l2 1.5" fill="none" stroke="#fff" stroke-width="1.5"/></svg>10:00AM</span></p>
    <div class="venue">
      <svg width="24" height="26" viewBox="0 0 24 26"><circle cx="12" cy="12" r="11" fill="none" stroke="#f08c1a" stroke-width="2"/><path d="M12 19c-3-4-4.5-6-4.5-8a4.5 4.5 0 0 1 9 0c0 2-1.5 4-4.5 8z" fill="#f08c1a"/><circle cx="12" cy="11" r="1.6" fill="#12345c"/></svg>
      <p>Lindqvist Community Center,<br>482 Tamsworth Street,<br>Portland, ME 04102</p>
    </div>
  </section>
  <div class="band-rule bottom"></div>

  <ul class="contact">
    <li><svg width="16" height="12" viewBox="0 0 16 12"><rect width="16" height="12" fill="#f08c1a"/><path d="M0 0l8 6 8-6" fill="none" stroke="#fff" stroke-width="1.2"/></svg>contact@cedarbrookfellowship.org</li>
    <li><svg width="16" height="16" viewBox="0 0 16 16"><path d="M3 1l3 3-2 2c1 2 3 4 5 5l2-2 3 3-2 3C7 15 1 9 1 3z" fill="#f08c1a"/></svg>207 555 0148</li>
    <li><svg width="16" height="16" viewBox="0 0 16 16"><circle cx="8" cy="8" r="7" fill="none" stroke="#f08c1a" stroke-width="1.4"/><ellipse cx="8" cy="8" rx="3" ry="7" fill="none" stroke="#f08c1a" stroke-width="1.2"/><path d="M1 8h14" stroke="#f08c1a" stroke-width="1.2"/></svg>http://corvane.org/</li>
  </ul>

  <div class="speaker-photo" role="img" aria-label="Portrait photo of the speaker in a dark blazer, seated and smiling"></div>
</article>
</body>
</html>
```